REAL ESTATE MAILBOX DROP FLYER

I am looking for two flyer designs. One for DL and one for A4 size. My company is a boutique real estate agency that offers a full/high quality service at a very low commission rate.

Key Phrases to be included

A4 Design should have a space for some text and a table in the center (outline below)

Target Market(s)

Home Owners

Industry/Entity Type

Real Estate Agent

Colors
0455a3

Requirements
Must have
• Eye Catching
• Bold
• high end feel
• Color pallette should match the logo
• The feel of the brochures must convey a trustworthy, high end service.
• Must be eye catching and easy to read
• Editable file formats must be supplied

```html
<!DOCTYPE html>
<html lang="en">
<head>
<meta charset="utf-8">
<title>Tenth Mark Realty – DL Flyer</title>
<link href="https://fonts.googleapis.com/css2?family=Montserrat:wght@700;800&family=Raleway:wght@300;400;600&family=Tinos:wght@400;700&display=swap" rel="stylesheet">
<style>
  :root{
    --navy:#0e2241;
    --copper:#a3704e;
    --white:#ffffff;
    --ink:#1d1d1d;
    --rule:#8a8a8a;
    --table-head:#d3d3d3;
    --backdrop:#e8e8e8;
  }
  *{box-sizing:border-box;margin:0;padding:0}
  html,body{width:1150px;height:1200px;overflow:hidden;background:var(--backdrop)}
  .flyer{
    position:absolute;left:42px;top:333px;width:1066px;height:533px;
    background:var(--white);overflow:hidden;
    box-shadow:0 18px 24px -14px rgba(0,0,0,.45);
    font-family:"Raleway",sans-serif;color:var(--ink);
  }
  .top-band{position:absolute;left:0;top:0;width:1066px;height:168px;background:var(--navy)}
  .house-art{position:absolute;left:0;top:0}
  .small-photo{
    position:absolute;top:313px;width:227px;height:112px;
    border:4px solid var(--white);
    box-shadow:0 10px 10px -6px rgba(0,0,0,.35);
  }
  .small-photo.bedroom{left:27px;background:linear-gradient(160deg,#e6e4e0 0%,#b9b6b2 55%,#5a5b5f 100%)}
  .small-photo.kitchen{left:277px;background:linear-gradient(160deg,#ecebe8 0%,#c7b49a 55%,#8a6a48 100%)}
  .brand{
    position:absolute;left:18px;top:40px;width:140px;
    color:var(--white);font-family:"Raleway",sans-serif;font-weight:400;
    font-size:19px;line-height:19px;text-align:center;letter-spacing:.5px;
  }
  .headline{position:absolute;left:530px;top:38px;color:var(--white);font-family:"Montserrat",sans-serif;font-weight:800}
  .headline .lead{font-size:22px;line-height:29px}
  .headline .key{font-size:33px;line-height:36px;margin-top:1px}
  .rate{
    position:absolute;left:636px;top:26px;font-family:"Montserrat",sans-serif;font-weight:800;
    color:var(--copper);font-size:74px;line-height:80px;
  }
  .save-tag{
    position:absolute;left:764px;top:64px;width:268px;height:34px;
    background:var(--white);border-radius:6px;color:var(--navy);
    font-size:29px;line-height:34px;text-align:center;
  }
  .save-tag b,.save-sub b{font-weight:600}
  .save-sub{position:absolute;left:766px;top:99px;width:266px;color:var(--white);font-size:27px;line-height:34px;text-align:right}
  .intro{
    position:absolute;left:561px;top:184px;width:471px;
    font-size:13px;line-height:16px;text-align:justify;
  }
  .stats{
    position:absolute;left:561px;top:266px;width:471px;border-collapse:collapse;
    font-family:"Tinos",serif;font-size:9.5px;color:var(--ink);
  }
  .stats th{font-weight:700;height:20px;background:var(--table-head)}
  .stats th.var{text-align:left;padding-left:42px}
  .stats th span{display:block;border-top:1px solid var(--rule);border-bottom:1px solid var(--rule);margin:0 6px}
  .stats td{height:15px;text-align:center}
  .stats td.label{text-align:left;vertical-align:middle}
  .stats tr.group-end td{border-bottom:1px solid var(--rule)}
  .stats tr.group-end td.label{border-bottom:1px solid var(--rule)}
  .contact-line{position:absolute;left:25px;top:450px;color:var(--navy);font-size:26px;font-weight:400;line-height:32px}
  .appraisal{
    position:absolute;left:25px;top:486px;width:266px;height:32px;background:var(--navy);
    color:var(--white);font-size:21px;line-height:32px;padding-left:6px;
  }
  .appraisal b{font-weight:600}
  .phone-block{
    position:absolute;left:291px;top:446px;width:260px;height:87px;background:var(--navy);
    color:var(--white);font-family:"Tinos",serif;font-weight:700;font-size:40px;line-height:87px;text-align:center;
  }
  .promise-block{
    position:absolute;left:554px;top:446px;width:512px;height:87px;background:var(--navy);
    color:var(--white);text-align:right;padding-right:34px;
  }
  .promise-block .tagline{font-size:26px;line-height:30px;margin-top:14px;font-weight:300}
  .promise-block .tagline b{font-weight:600}
  .promise-block .web{font-size:14px;line-height:20px;margin-top:2px}
  .promise-block .web b{font-weight:600}
</style>
</head>
<body>
<main class="flyer">
  <div class="top-band"></div>

  <svg class="house-art" width="560" height="360" viewBox="0 0 560 360">
    <polygon points="26,172 26,150 284,12 534,150 534,172" fill="#ffffff"/>
    <defs>
      <linearGradient id="living" x1="0" y1="0" x2="0" y2="1">
        <stop offset="0" stop-color="#e9e8e5"/>
        <stop offset=".55" stop-color="#bdbcb9"/>
        <stop offset="1" stop-color="#8e8d8b"/>
      </linearGradient>
    </defs>
    <polygon role="img" aria-label="Photo of a bright living and dining room"
      points="0,353 0,172 34,172 34,156 284,22 526,156 526,353" fill="url(#living)"/>
  </svg>

  <div class="small-photo bedroom" role="img" aria-label="Photo of a made-up bedroom"></div>
  <div class="small-photo kitchen" role="img" aria-label="Photo of an open kitchen and lounge"></div>

  <div class="brand">TENTH MARK<br>REALTY</div>

  <div class="headline">
    <div class="lead">Top Tier<br>Service,</div>
    <div class="key">Commission</div>
  </div>
  <div class="rate">1%</div>
  <div class="save-tag">Save <b>THOUSANDS</b></div>
  <div class="save-sub">On <b>COMMISSIONS!</b></div>

  <p class="intro">Lorem ipsum dolor sit amet, consectetur adipiscing elit, sed do eiusmod tempor incididunt ut abore et dolore magna aliqua. Ut enim ad minim veniam, quis nostrud exercitation ullamco laboris nisi ut aliquip ex ea commodo consequat.</p>

  <table class="stats">
    <thead>
      <tr><th class="var" rowspan="2">Variable</th><th></th><th><span>(n=32)</span></th><th><span>(n=52)</span></th></tr>
      <tr><th></th><th>Freq. (%)</th><th>Freq. (%)</th></tr>
    </thead>
    <tbody>
      <tr><td class="label" rowspan="2">Relationship</td><td>No</td><td>75</td><td>96</td></tr>
      <tr class="group-end"><td>Yes</td><td>25</td><td>4</td></tr>
      <tr><td class="label" rowspan="2">Agricultural newsletter</td><td>No</td><td>47</td><td>81</td></tr>
      <tr class="group-end"><td>Yes</td><td>53</td><td>19</td></tr>
      <tr><td class="label" rowspan="2">Certification experience</td><td>No</td><td>63</td><td>94</td></tr>
      <tr class="group-end"><td>Yes</td><td>38</td><td>6</td></tr>
      <tr><td class="label" rowspan="2">Life experience</td><td>No</td><td>56</td><td>85</td></tr>
      <tr class="group-end"><td>Yes</td><td>44</td><td>15</td></tr>
    </tbody>
  </table>

  <div class="contact-line">Contact Marcus today</div>
  <div class="appraisal">for a <b>FREE APPRAISAL!</b></div>
  <div class="phone-block">0400 318 627</div>
  <div class="promise-block">
    <div class="tagline">More <b>Money</b> in YOUR Pocket!</div>
    <div class="web">marcus@<b>tenthmarkrealty</b>.com.au | www.<b>tenthmarkrealty</b>.com.au</div>
  </div>
</main>
</body>
</html>
```